UPDATE 2: I HAVE ATTACHED TWO PHOTOS; PLEASE CONSIDER USING EITHER ONE IN A NEW DESIGN. THANK YOU.
UPDATE: I HAVE INCLUDED 4 SAMPLE BOOK COVERS THAT I LIKE TO HELP YOU ORIENT YOUR DESIGN WORK
Looking for book cover, spine, and back for a MEMOIR. Details:
TITLE: Mama's Quiet Orchard
AUTHOR: Lorivel Brashton
GENRE: Memoir
STYLE REQUESTED: Abstract and colorful; designers are welcome to get creative. Note that the memoir takes place largely in a poor African American city.
BOOK SUMMARY: As a young girl, Lorivel Brashton—or “Rivvy” to her friends and family—discovers the man she thought was her father wasn’t, and her real biological father wants little if anything to do with her. What follows is the story of a girl’s longing, a longing disturbed by abuse, disappointment, and loneliness.
Set against the backdrop of Gary, Indiana—the then “murder capital of the world”—Mama’s Quiet Orchard follows Lorivel as she searches and grows, following a path that eventually leads her to self-discovery and self-confidence.
Template provided for InDesign. Please note margins and bleed areas. Make sure any letters/words are at least one inch from edges. On spine, leave three inches at bottom for publisher's logo.
Updates
To all designers: Please note that there should NOT be any images of people as part of your designs. Thank you, and my apologies for not mentioning that in the initial ask.

```html
<!DOCTYPE html>
<html lang="en">
<head>
<meta charset="utf-8">
<title>Mama's Quiet Orchard — Cover</title>
<link rel="stylesheet" href="https://fonts.googleapis.com/css2?family=Saira+Semi+Condensed:wght@700&family=Montserrat:wght@400;500&display=swap">
<style>
  :root {
    --page: #ffffff;
    --cover-black: #050505;
    --ink-light: #ffffff;
    --art-orange: #d9642a;
    --art-cream: #e8d3b0;
    --art-blue: #3f7fb8;
    --art-rust: #8a2f1c;
  }
  * { margin: 0; padding: 0; box-sizing: border-box; }
  html, body {
    width: 1155px;
    height: 1200px;
    overflow: hidden;
    background: var(--page);
  }
  .canvas {
    position: relative;
    width: 1155px;
    height: 1200px;
    background: var(--page);
  }
  .book-cover {
    position: absolute;
    left: 269px;
    top: 141px;
    width: 608px;
    height: 915px;
    background: var(--cover-black);
    overflow: hidden;
  }
  .cover-title {
    position: absolute;
    left: 0;
    top: 48px;
    width: 100%;
    text-align: center;
    font-family: "Saira Semi Condensed", "Arial Narrow", sans-serif;
    font-weight: 700;
    font-size: 58px;
    line-height: 62px;
    letter-spacing: 1px;
    color: var(--ink-light);
    text-transform: uppercase;
  }
  .cover-genre {
    position: absolute;
    left: 421px;
    top: 218px;
    font-family: "Montserrat", Arial, sans-serif;
    font-weight: 400;
    font-size: 28px;
    color: var(--ink-light);
  }
  .cover-art {
    position: absolute;
    left: 6px;
    top: 300px;
    width: 596px;
    height: 612px;
    background:
      radial-gradient(ellipse at 72% 42%, var(--art-cream) 0%, rgba(232,211,176,0.6) 18%, transparent 45%),
      radial-gradient(ellipse at 30% 35%, var(--art-blue) 0%, rgba(63,127,184,0.5) 20%, transparent 48%),
      radial-gradient(ellipse at 25% 75%, var(--art-orange) 0%, rgba(217,100,42,0.55) 25%, transparent 55%),
      radial-gradient(ellipse at 60% 85%, var(--art-rust) 0%, transparent 50%),
      var(--cover-black);
  }
  .cover-author {
    position: absolute;
    left: 0;
    top: 828px;
    width: 100%;
    text-align: center;
    font-family: "Montserrat", Arial, sans-serif;
    font-weight: 500;
    font-size: 45px;
    color: var(--ink-light);
  }
</style>
</head>
<body>
  <div class="canvas">
    <div class="book-cover">
      <div class="cover-art" role="img" aria-label="Abstract swirling painting in orange, cream, blue and rust tones on black"></div>
      <h1 class="cover-title">Mama's Quiet<br>Orchard</h1>
      <p class="cover-genre">Memoir</p>
      <p class="cover-author">Lorivel Brashton</p>
    </div>
  </div>
</body>
</html>
```